Musician website

I need a website developed for a musician

The style and content of the website were are looking for is like :

https://www.corvantellisounds.example/
https://www.grindolax.example/
https://www.mirelwandby.example/
https://www.olbrenquist.example/?frontpage=true

The name of the musician is 'Tamsin Orlebo'

Attached are some professional photos to use

Number of Pages Required

1 page

```html
<!DOCTYPE html>
<html lang="en">
<head>
<meta charset="utf-8">
<title>Tamsin Orlebo — Musician</title>
<link rel="stylesheet" href="https://fonts.googleapis.com/css2?family=Abril+Fatface&family=Playfair+Display:wght@700;900&family=Poppins:wght@500;600;700&family=Open+Sans:wght@400;600;700&display=swap">
<style>
:root{
  --ink:#111111;
  --white:#ffffff;
  --line:#222222;
  --blog-bg:#f5f1f1;
  --footer:#0b0b0b;
  --accent:#e8731b;
  --muted:#333333;
  --hero-a:#3d4a35;
  --hero-b:#2a2a26;
}
*{margin:0;padding:0;box-sizing:border-box}
html,body{width:1200px;height:4488px;overflow:hidden}
body{font-family:"Open Sans",sans-serif;color:var(--ink);background:var(--white);position:relative}
.section{position:absolute;left:0;width:1200px;overflow:hidden}
.abs{position:absolute}
.photo{position:absolute}

/* Hero */
.hero{top:0;height:698px}
.hero .photo{inset:0;background:radial-gradient(ellipse at 50% 40%,#5e6150 0%,var(--hero-a) 40%,var(--hero-b) 100%)}
.hero-shade{position:absolute;inset:0;background:linear-gradient(90deg,rgba(0,0,0,.35),rgba(0,0,0,0) 50%)}
.brand{font-family:"Poppins",sans-serif;font-weight:600;font-size:25px;color:var(--white)}
.hero .brand{left:38px;top:22px}
.nav{display:flex;font-family:"Poppins",sans-serif;font-weight:500;font-size:13px;color:var(--white);letter-spacing:.3px}
.nav span{position:absolute;white-space:nowrap}
.hero-welcome{left:95px;top:370px;font-family:"Poppins",sans-serif;font-weight:600;font-size:28px;color:var(--white)}
.hero-name{left:94px;top:404px;font-family:"Poppins",sans-serif;font-weight:700;font-size:39px;color:var(--white)}
.btn{position:absolute;border:2px solid var(--white);color:var(--white);font-family:"Poppins",sans-serif;font-weight:600;font-size:13px;display:flex;align-items:center;justify-content:center;letter-spacing:.3px}
.hero .btn{left:96px;top:477px;width:116px;height:42px}
.dots{left:561px;top:653px;display:flex;gap:10px}
.dots i{display:block;width:7px;height:7px;border-radius:50%;background:var(--white)}
.dots i.on{background:var(--accent)}

/* Tour */
.tour{top:698px;height:716px}
.label-box{position:absolute;border:1.5px solid var(--ink);font-size:21px;display:flex;align-items:center;justify-content:center;letter-spacing:.3px}
.tour .label-box{left:132px;top:68px;width:174px;height:61px}
.event{position:absolute;width:234px}
.event .date{font-size:13px;letter-spacing:.3px}
.event .city{font-family:"Playfair Display",serif;font-weight:900;font-size:17px;margin-top:6px}
.event .desc{font-size:12px;margin-top:6px}
.event .links{display:flex;gap:22px;margin-top:18px;font-family:"Poppins",sans-serif;font-weight:700;font-size:10.5px;text-decoration:underline;padding-left:2px}
.event .rule{position:absolute;left:0;top:126px;width:234px;height:2px;background:var(--line)}
.tour .photo{left:690px;top:65px;width:378px;height:576px;background:linear-gradient(160deg,#5f7f74 0%,#c9c4ba 45%,#3a2f2a 100%)}

/* About */
.about{top:1414px;height:566px}
.about .photo{inset:0;background:linear-gradient(90deg,#15140f 0%,#2a2a22 45%,#3b3a2e 70%,#1e1d18 100%)}
.about .label-box{left:132px;top:138px;width:126px;height:38px;border-color:var(--white);color:var(--white);font-size:17px}
.about-title{left:132px;top:198px;width:380px;font-family:"Playfair Display",serif;font-weight:900;font-size:28px;line-height:38px;color:var(--white)}
.about-text{left:134px;top:326px;width:370px;font-size:17px;line-height:22px;color:#eeeeee}
.about .btn{left:138px;top:438px;width:116px;height:40px}

/* Videos */
.videos{top:1980px;height:673px;background:#141414}
.videos-bg{position:absolute;left:0;top:154px;width:1200px;height:519px;background:linear-gradient(90deg,#1b1e20,#2a2a28 50%,#17191b)}
.section-title{position:absolute;left:0;width:1200px;text-align:center;font-family:"Abril Fatface",serif;font-size:48px}
.videos .section-title{top:48px;color:var(--white)}
.videos .photo{left:235px;top:154px;width:730px;height:451px;background:radial-gradient(ellipse at 50% 25%,#d9d2c4 0%,#6b5b4b 35%,#1b1714 80%)}
.play{left:553px;top:2400px}
.play-label{left:0;width:1180px;top:500px;text-align:center;color:var(--white);font-size:12px;letter-spacing:.5px}

/* Photos */
.photos{top:2653px;height:1039px}
.photos .section-title{top:48px}

/* Blog */
.blog{top:3692px;height:619px;background:var(--blog-bg)}
.blog .section-title{top:45px}
.card{position:absolute;top:150px;width:302px;height:416px;background:var(--white)}
.card .photo{left:0;top:0;width:302px;height:172px}
.card h3{position:absolute;left:27px;top:208px;width:250px;font-family:"Playfair Display",serif;font-weight:900;font-size:15px;line-height:26px}
.card p{position:absolute;left:27px;top:274px;width:250px;font-size:12px;line-height:19px;color:var(--muted)}
.card .card-btn{position:absolute;left:27px;top:354px;width:80px;height:30px;border:1.5px solid var(--ink);font-family:"Poppins",sans-serif;font-weight:600;font-size:9px;display:flex;align-items:center;justify-content:center}

/* Footer */
.footer{top:4311px;height:177px;background:var(--footer)}
.footer .brand{left:132px;top:38px}
.footer-rule{left:132px;top:95px;width:936px;height:1px;background:#444}
.copyright{left:0;width:1200px;top:141px;text-align:center;font-size:11px;color:#cccccc}
</style>
</head>
<body>

<section class="section hero">
  <div class="photo" role="img" aria-label="Musician seated on garden stone steps playing an electric guitar"></div>
  <div class="hero-shade"></div>
  <div class="abs brand">Tamsin Orlebo</div>
  <nav class="nav">
    <span style="left:662px;top:28px">HOME</span>
    <span style="left:740px;top:28px">ABOUT ME</span>
    <span style="left:846px;top:28px">MUSIC</span>
    <span style="left:928px;top:28px">VIDEOS</span>
    <span style="left:1022px;top:28px">EVENTS</span>
    <span style="left:1107px;top:28px">PHOTOS</span>
  </nav>
  <div class="abs hero-welcome">Welcome to</div>
  <h1 class="abs hero-name">Tamsin Orlebo</h1>
  <div class="btn">READ MORE</div>
  <div class="abs dots"><i></i><i></i><i class="on"></i><i></i><i></i></div>
</section>

<section class="section tour">
  <div class="label-box">TOUR DATES</div>

  <div class="event" style="left:132px;top:175px">
    <div class="date">NOV 27, 2021</div>
    <div class="city">Arlington, TX, United States</div>
    <div class="desc">Lorem Ipsum is simply dummy text</div>
    <div class="links"><span>TICKET</span><span>MORE INFO</span></div>
    <div class="rule"></div>
  </div>
  <div class="event" style="left:423px;top:175px">
    <div class="date">DEC 27, 2021</div>
    <div class="city">San Francisco, CA</div>
    <div class="desc">Lorem Ipsum is simply dummy text</div>
    <div class="links"><span>TICKET</span><span>MORE INFO</span></div>
    <div class="rule"></div>
  </div>
  <div class="event" style="left:132px;top:342px">
    <div class="date">JAN 02, 2022</div>
    <div class="city">Glendale, AZ, USA</div>
    <div class="desc">Lorem Ipsum is simply dummy text</div>
    <div class="links"><span>TICKET</span><span>MORE INFO</span></div>
    <div class="rule"></div>
  </div>
  <div class="event" style="left:427px;top:342px">
    <div class="date">JAN 02, 2022</div>
    <div class="city">Glendale, AZ, USA</div>
    <div class="desc">Lorem Ipsum is simply dummy text</div>
    <div class="links"><span>TICKET</span><span>MORE INFO</span></div>
    <div class="rule" style="left:-4px"></div>
  </div>
  <div class="event" style="left:132px;top:517px">
    <div class="date">NOV 27, 2021</div>
    <div class="city">Arlington, TX, United States</div>
    <div class="desc">Lorem Ipsum is simply dummy text</div>
    <div class="links"><span>TICKET</span><span>MORE INFO</span></div>
  </div>
  <div class="event" style="left:423px;top:517px">
    <div class="date">DEC 27, 2021</div>
    <div class="city">San Francisco, CA</div>
    <div class="desc">Lorem Ipsum is simply dummy text</div>
    <div class="links"><span>TICKET</span><span>MORE INFO</span></div>
  </div>

  <div class="photo" role="img" aria-label="Musician in a white shirt holding a white electric guitar beside a pool"></div>
</section>

<section class="section about">
  <div class="photo" role="img" aria-label="Musician in a dark denim jacket leaning against large boulders"></div>
  <div class="label-box">ABOUT ME</div>
  <h2 class="abs about-title">Lorem Ipsum is simply dummy text of the printing and typesetting</h2>
  <p class="abs about-text">There are many variations of passages of Lorem Ipsum available, but the majority have suffered alteration in some form, by injected humour, or randomised words.</p>
  <div class="btn">READ MORE</div>
</section>

<section class="section videos">
  <div class="videos-bg" role="img" aria-label="Dimmed background scene of the musician by a pool"></div>
  <h2 class="section-title">Videos</h2>
  <div class="photo" role="img" aria-label="Video still of the musician facing a bright curtained window"></div>
  <svg class="abs" style="left:556px;top:420px" width="66" height="66" viewBox="0 0 66 66" aria-hidden="true">
    <circle cx="33" cy="33" r="30" fill="none" stroke="#ffffff" stroke-width="4"/>
    <path d="M26 20 L46 33 L26 46 Z" fill="none" stroke="#ffffff" stroke-width="4" stroke-linejoin="round"/>
  </svg>
  <div class="abs play-label">PLAY VIDEO</div>
</section>

<section class="section photos">
  <h2 class="section-title">Photos</h2>
  <div class="photo" style="left:132px;top:160px;width:458px;height:430px;background:linear-gradient(180deg,#d8d4c8 0%,#a8b6a0 45%,#4a8fb0 60%,#e8e4da 100%)" role="img" aria-label="Musician reclining on a lounge chair by a pool"></div>
  <div class="photo" style="left:611px;top:160px;width:457px;height:430px;background:linear-gradient(180deg,#e9e9e7 0%,#cfcfcb 50%,#2a2a2a 80%,#e0e0dc 100%)" role="img" aria-label="Musician in a cap playing guitar on a white bench"></div>
  <div class="photo" style="left:132px;top:609px;width:302px;height:357px;background:linear-gradient(180deg,#c9cfd2 0%,#8e9a86 55%,#2f3b26 100%)" role="img" aria-label="Musician dunking a basketball"></div>
  <div class="photo" style="left:449px;top:609px;width:302px;height:357px;background:linear-gradient(180deg,#ecebe6 0%,#b4aea2 40%,#1c1c1c 100%)" role="img" aria-label="Musician playing a piano"></div>
  <div class="photo" style="left:768px;top:609px;width:300px;height:357px;background:linear-gradient(180deg,#2d2b2a 0%,#1f2a58 55%,#1b2550 100%)" role="img" aria-label="Musician lying on a pool table with billiard balls"></div>
</section>

<section class="section blog">
  <h2 class="section-title">Latest Blog</h2>
  <article class="card" style="left:132px">
    <div class="photo" style="background:linear-gradient(180deg,#e6e2da,#1c1c1c 60%,#5a3a24)" role="img" aria-label="Musician at a grand piano"></div>
    <h3>Lorem Ipsum is simply dummy text of the printing</h3>
    <p>There are many variations of passages of Lorem Ipsum available, but the majority have suffered alteration in some form, by injected humour.</p>
    <div class="card-btn">READ MORE</div>
  </article>
  <article class="card" style="left:449px">
    <div class="photo" style="background:linear-gradient(180deg,#ecebe8,#c9c8c3 55%,#2a2a2a)" role="img" aria-label="Musician playing guitar on a white bench"></div>
    <h3>Lorem Ipsum is simply dummy text of the printing</h3>
    <p>There are many variations of passages of Lorem Ipsum available, but the majority have suffered alteration in some form, by injected humour.</p>
    <div class="card-btn">READ MORE</div>
  </article>
  <article class="card" style="left:768px">
    <div class="photo" style="background:linear-gradient(180deg,#dfe3e2,#7f9670 55%,#3a3a36)" role="img" aria-label="Musician in a cap outdoors by a house"></div>
    <h3>Lorem Ipsum is simply dummy text of the printing</h3>
    <p>There are many variations of passages of Lorem Ipsum available, but the majority have suffered alteration in some form, by injected humour.</p>
    <div class="card-btn">READ MORE</div>
  </article>
</section>

<footer class="section footer">
  <div class="abs brand">Tamsin Orlebo</div>
  <nav class="nav">
    <span style="left:568px;top:42px">HOME</span>
    <span style="left:646px;top:42px">ABOUT ME</span>
    <span style="left:752px;top:42px">MUSIC</span>
    <span style="left:835px;top:42px">VIDEOS</span>
    <span style="left:929px;top:42px">EVENTS</span>
    <span style="left:1013px;top:42px">PHOTOS</span>
  </nav>
  <div class="abs footer-rule"></div>
  <div class="abs copyright">Copyright © 2021 All Rights Reserved</div>
</footer>

</body>
</html>
```